Surviving Domestic Violence Flyer

I need a flyer that "POPS" to attract participants for my research project. I have added the important information on my draft flyer.

```html
<!DOCTYPE html>
<html lang="en">
<head>
<meta charset="utf-8">
<title>Request for Study Participants</title>
<link rel="stylesheet" href="https://fonts.googleapis.com/css2?family=Oswald:wght@500&family=Arimo:wght@400;700&display=swap">
<style>
  :root {
    --page: #ffffff;
    --ink-dark: #0b0b0b;
    --ink-mid: #1c1c1c;
    --teal: #11a9a9;
    --white: #ffffff;
    --soft: #d9d9d9;
    --photo-light: #6f8586;
    --photo-mid: #2e3a3b;
  }
  * { margin: 0; padding: 0; box-sizing: border-box; }
  html, body {
    width: 1200px; height: 900px; overflow: hidden;
    background: var(--page);
  }
  .flyer {
    position: absolute; left: 269px; top: 5px;
    width: 675px; height: 875px;
    background: radial-gradient(ellipse at 55% 35%, var(--ink-mid) 0%, var(--ink-dark) 75%);
    overflow: hidden;
    font-family: "Arimo", Arial, sans-serif;
    color: var(--white);
  }
  .flyer > * { position: absolute; white-space: nowrap; line-height: 1.2; }
  .title {
    left: 0; width: 100%; top: 18px; text-align: center;
    font-family: "Oswald", "Arial Narrow", sans-serif; font-weight: 500;
    font-size: 54px; line-height: 1.25; color: var(--teal);
    letter-spacing: 0.2px;
  }
  .subtitle {
    left: 0; width: 100%; top: 87px; text-align: center;
    font-weight: 700; font-size: 14.6px; letter-spacing: 0.3px;
  }
  .question { left: 103px; font-size: 17.5px; }
  .question.teal { color: var(--teal); }
  .q1 { top: 142px; } .q2 { top: 175px; } .q3 { top: 206px; }
  .q4 { top: 241px; } .q5 { top: 274px; line-height: 21px; white-space: normal; width: 500px; }
  .eligibility {
    left: 37px; top: 352px; width: 600px; white-space: normal;
    font-size: 12.4px; line-height: 15px; color: var(--soft);
  }
  .photo {
    left: 0; top: 398px; width: 320px; height: 328px;
    background:
      radial-gradient(ellipse at 55% 70%, var(--photo-light) 0%, var(--photo-mid) 45%, transparent 80%),
      linear-gradient(90deg, var(--ink-dark) 0%, transparent 30%);
  }
  .contact { left: 331px; }
  .contact-lead { top: 433px; font-size: 20px; }
  .contact-phone { left: 372px; top: 459px; font-size: 25px; }
  .contact-small { font-size: 12.4px; }
  .c-email { top: 488px; }
  .c-more { top: 503px; }
  .c-paid { top: 546px; }
  .c-l1 { top: 590px; } .c-l2 { top: 605px; } .c-l3 { top: 620px; }
  .c-l4 { top: 634px; } .c-l5 { top: 649px; } .c-l6 { top: 663px; }
  .teal { color: var(--teal); }
  .tear-strip {
    left: 0; top: 726px; width: 100%; height: 149px;
    display: flex; border-top: 1px solid var(--soft);
  }
  .tab {
    flex: 1; display: flex; flex-direction: column; align-items: center; justify-content: center;
    border-left: 1px solid var(--soft);
  }
  .tab:first-child { border-left: none; }
  .tab-text {
    writing-mode: vertical-rl; transform: rotate(180deg);
    display: flex; flex-direction: column-reverse; gap: 1px; align-items: flex-start;
    font-weight: 700; text-align: left;
  }
  .tab-name { font-size: 9.6px; }
  .tab-phone { font-size: 13px; }
</style>
</head>
<body>
  <main class="flyer">
    <h1 class="title">Request for Study Participants</h1>
    <p class="subtitle">EFFICIENCY OF RESOURCES AVAILABLE TO SUVIVORS OF INTIMATE PARTNER ABUSE</p>

    <p class="question teal q1">Are you eighteen years of age or older?</p>
    <p class="question q2">Have you been a victim of domestic violence?</p>
    <p class="question teal q3">Have you sought assistance with abuse in last 12 months?</p>
    <p class="question q4">Are you still in contact with person who abused you?</p>
    <p class="question teal q5">Are you willing and open to discussing your expirience with abuse and your attempts to access services or resources?</p>

    <p class="eligibility">If you answered yes to all of these questions, you may be eligible to participate in a study to better understand the resources needed and services expected for survivors of domestic violence.</p>

    <div class="photo" role="img" aria-label="Photograph of a woman seated on the floor hugging her knees in a dark room while a hand rests on her shoulder"></div>

    <p class="contact contact-lead">Please contact Dana Whitfield at</p>
    <p class="contact-phone">1(773)555-0142</p>
    <p class="contact contact-small c-email">via e-mail <span class="teal">survivorvoices.study@mailbox.org</span></p>
    <p class="contact contact-small c-more">for additional information.</p>
    <p class="contact contact-small c-paid">Participants will be comensated for their time.</p>
    <p class="contact contact-small teal c-l1">Principal Investigator:</p>
    <p class="contact contact-small c-l2">Dana Whitfield</p>
    <p class="contact contact-small c-l3">Institutional Affiliation: Lakeshore State University,</p>
    <p class="contact contact-small c-l4">Dept. of Criminology, Law and Justice</p>
    <p class="contact contact-small teal c-l5">Contact Address:</p>
    <p class="contact contact-small c-l6">Post Office Box 551208, Chicago, IL, 60615</p>

    <div class="tear-strip">
      <div class="tab"><div class="tab-text"><span class="tab-name">Survivor Resources Study</span><span class="tab-phone">1(773)555-0142</span></div></div>
      <div class="tab"><div class="tab-text"><span class="tab-name">Survivor Resources Study</span><span class="tab-phone">1(773)555-0142</span></div></div>
      <div class="tab"><div class="tab-text"><span class="tab-name">Survivor Resources Study</span><span class="tab-phone">1(773)555-0142</span></div></div>
      <div class="tab"><div class="tab-text"><span class="tab-name">Survivor Resources Study</span><span class="tab-phone">1(773)555-0142</span></div></div>
      <div class="tab"><div class="tab-text"><span class="tab-name">Survivor Resources Study</span><span class="tab-phone">1(773)555-0142</span></div></div>
      <div class="tab"><div class="tab-text"><span class="tab-name">Survivor Resources Study</span><span class="tab-phone">1(773)555-0142</span></div></div>
      <div class="tab"><div class="tab-text"><span class="tab-name">Survivor Resources Study</span><span class="tab-phone">1(773)555-0142</span></div></div>
      <div class="tab"><div class="tab-text"><span class="tab-name">Survivor Resources Study</span><span class="tab-phone">1(773)555-0142</span></div></div>
      <div class="tab"><div class="tab-text"><span class="tab-name">Survivor Resources Study</span><span class="tab-phone">1(773)555-0142</span></div></div>
      <div class="tab"><div class="tab-text"><span class="tab-name">Survivor Resources Study</span><span class="tab-phone">1(773)555-0142</span></div></div>
      <div class="tab"><div class="tab-text"><span class="tab-name">Survivor Resources Study</span><span class="tab-phone">1(773)555-0142</span></div></div>
      <div class="tab"><div class="tab-text"><span class="tab-name">Survivor Resources Study</span><span class="tab-phone">1(773)555-0142</span></div></div>
      <div class="tab"><div class="tab-text"><span class="tab-name">Survivor Resources Study</span><span class="tab-phone">1(773)555-0142</span></div></div>
    </div>
  </main>
</body>
</html>
```